Simple and Clean business card design

We would like the design to be simple clean and to incorporate our colors.

We are open to your design and talent, we have the dots in our logo as we think of it as data points and we connect data points for people.

We are open to see the great creative and clean design you bring to the table

Contact Information for Business Card

please include: name, position, email, phone and website

Font styles to use
Sans Serif

Requirements
Must have
• my colors incorporated, simplicity
Nice to have
• lots of white space, simplicity
Should not have
• complexicity/ complex art

```html
<!DOCTYPE html>
<html lang="en">
<head>
<meta charset="utf-8">
<title>Nectra Business Card</title>
<link rel="stylesheet" href="https://fonts.googleapis.com/css2?family=Montserrat:wght@400;600;700;800&display=swap">
<style>
  :root {
    --stage: #2e2e2e;
    --paper: #ffffff;
    --ink: #111111;
    --ink-soft: #333333;
    --brand-blue: #4285f4;
    --brand-green: #34a853;
    --brand-yellow: #fbbc05;
    --brand-red: #ea4335;
    --brand-orange: #f7931e;
  }
  * { box-sizing: border-box; margin: 0; padding: 0; }
  html, body {
    width: 1200px;
    height: 866px;
    overflow: hidden;
    background: var(--stage);
    font-family: "Montserrat", sans-serif;
  }
  .stage {
    width: 1200px;
    height: 866px;
    display: flex;
    flex-direction: column;
    align-items: center;
    justify-content: center;
    gap: 40px;
  }
  .card {
    position: relative;
    width: 620px;
    height: 354px;
    border-radius: 4px;
    overflow: hidden;
    box-shadow: 0 14px 30px rgba(0, 0, 0, 0.45);
  }

  /* Front */
  .card-front { background: var(--paper); }
  .contact {
    position: absolute;
    left: 44px;
    top: 112px;
    color: var(--ink);
  }
  .contact-name {
    font-size: 26px;
    font-weight: 800;
    letter-spacing: 0.3px;
    line-height: 1.1;
  }
  .contact-role {
    font-size: 15px;
    font-weight: 400;
    color: var(--ink-soft);
    margin-bottom: 16px;
  }
  .contact-list { list-style: none; }
  .contact-item {
    display: flex;
    align-items: center;
    gap: 10px;
    font-size: 15px;
    font-weight: 400;
    line-height: 1;
    margin-bottom: 9px;
  }
  .contact-icon {
    width: 20px;
    height: 20px;
    flex: none;
  }
  .web-name { color: var(--brand-blue); }

  .wordmark {
    display: flex;
    align-items: center;
    gap: 10px;
    font-weight: 800;
    color: var(--ink);
    letter-spacing: 1px;
    line-height: 1;
  }
  .wordmark-dot {
    border-radius: 50%;
    background: var(--brand-blue);
    flex: none;
  }
  .card-front .wordmark {
    position: absolute;
    right: 48px;
    top: 150px;
    font-size: 70px;
  }
  .card-front .wordmark-dot { width: 22px; height: 22px; }

  /* Back */
  .card-back .artwork {
    position: absolute;
    inset: 0;
    background:
      radial-gradient(ellipse 70% 80% at 30% 75%, var(--brand-green) 0%, rgba(52,168,83,0) 70%),
      linear-gradient(120deg, var(--brand-blue) 0%, var(--brand-green) 28%, var(--brand-yellow) 52%, var(--brand-red) 78%, var(--brand-orange) 100%);
  }
  .card-back .wordmark {
    position: absolute;
    left: 60px;
    top: 70px;
    font-size: 62px;
  }
  .card-back .wordmark-dot { width: 20px; height: 20px; }
</style>
</head>
<body>
<main class="stage">

  <section class="card card-front" aria-label="Business card front">
    <div class="contact">
      <p class="contact-name">Daniel Ross</p>
      <p class="contact-role">Founder/ CEO</p>
      <ul class="contact-list">
        <li class="contact-item">
          <svg class="contact-icon" viewBox="0 0 20 20" aria-hidden="true">
            <circle cx="10" cy="10" r="10" fill="var(--brand-green)"/>
            <path d="M7 5.5 L8.6 5.5 L9.3 8 L8.2 9 Q9 11 11 11.8 L12 10.7 L14.5 11.4 L14.5 13 Q14 14.5 12.5 14.5 Q6 13.5 5.5 7.5 Q5.5 6 7 5.5 Z" fill="#fff"/>
          </svg>
          <span>555-014-2290</span>
        </li>
        <li class="contact-item">
          <svg class="contact-icon" viewBox="0 0 20 20" aria-hidden="true">
            <circle cx="10" cy="10" r="10" fill="var(--brand-yellow)"/>
            <rect x="5" y="6.5" width="10" height="7" fill="none" stroke="#fff" stroke-width="1.4"/>
            <path d="M5 6.5 L10 10.5 L15 6.5" fill="none" stroke="#fff" stroke-width="1.4"/>
          </svg>
          <span>daniel.ross@nectra.one</span>
        </li>
        <li class="contact-item">
          <svg class="contact-icon" viewBox="0 0 20 20" aria-hidden="true">
            <circle cx="10" cy="10" r="10" fill="var(--brand-red)"/>
            <circle cx="10" cy="10" r="5" fill="none" stroke="#fff" stroke-width="1.2"/>
            <ellipse cx="10" cy="10" rx="2.2" ry="5" fill="none" stroke="#fff" stroke-width="1.2"/>
            <path d="M5 10 H15" stroke="#fff" stroke-width="1.2"/>
          </svg>
          <span>www.<span class="web-name">nectra</span>.one</span>
        </li>
      </ul>
    </div>
    <div class="wordmark">
      <span class="wordmark-dot"></span>
      <span class="wordmark-name">Nectra</span>
    </div>
  </section>

  <section class="card card-back" aria-label="Business card back">
    <div class="artwork" role="img" aria-label="Flowing colour wave in blue, green, yellow, red and orange with soft translucent circles"></div>
    <div class="wordmark">
      <span class="wordmark-dot"></span>
      <span class="wordmark-name">Nectra</span>
    </div>
  </section>

</main>
</body>
</html>
```